Online tuition webpage design needed

Hi,
We are starting up an online tuition website for non- English speakers wishing to take an QUOLT test.

The webpage must include a place for people to enroll online in the course.
The home page must have:
• room for a logo (coming shortly, blue in colour)
• different packages of online tuition and payvora
• tool bar showing different pages
• perhaps a video, small pictures

This is my site currently:-

www.lingvarotutors.example

as you can see, I am not very sure how to create a website … The large logo is what I would like to use, but I project has not been finalized yet. Please note, I don’t like the logo being that large!

Sites that are similar to what I am doing and like the design of are:

http://www.tesmarilearn.example.au/fees

https://www.brovaskill.example/index.php

http://www.pelgrimtutorkaspar.example.uk/index.html

http://www.quorvanexams.example/

One thing I need is a place for student s to enroll, and if possible, I would like to use quillet to create exercises for students.
Currently, my site is using pagecraftr. My preference is to use quillet for online activities. I am not sure if I can use both.
Thanks in advance

Target Market(s)

people wising to take an QUOLT test (English proficiency test)

Industry/Entity Type

Online

Colors
3276b5
0292cd

Requirements
Must have
• a place for enrollment and admin login for students
quillet
video
talqo, friendwall, chirplo logos
Nice to have
• a booking calender
Should not have
• too much clutter. must be clean and professional looking

```html
<!DOCTYPE html>
<html lang="en">
<head>
<meta charset="utf-8">
<title>QUOLT Online Tuition</title>
<link rel="stylesheet" href="https://fonts.googleapis.com/css2?family=Roboto:wght@300;400;500&family=Open+Sans:ital,wght@0,400;0,600;1,400&display=swap">
<style>
:root{
  --brand:#0292cd;
  --brand-deep:#3276b5;
  --navy:#0b2a57;
  --navy-dark:#08214a;
  --ink:#444;
  --muted:#666;
  --btn-dark:#4b5560;
  --line:#d9dde2;
  --band:#f1f2f3;
}
*{margin:0;padding:0;box-sizing:border-box}
html,body{width:800px;height:1200px;overflow:hidden}
body{position:relative;background:#fff;font-family:'Open Sans',sans-serif;color:var(--ink)}
.abs{position:absolute}
/* header */
.logo{left:108px;top:22px;display:flex;align-items:center;gap:8px}
.logo-mark{width:26px;height:26px;background:var(--brand-deep)}
.logo-name{font-family:'Roboto',sans-serif;font-weight:400;font-size:26px;color:var(--brand-deep);line-height:1}
.logo-sub{left:158px;top:55px;font-family:'Roboto',sans-serif;font-size:11px;color:var(--brand-deep)}
.social{top:12px;display:flex;gap:5px;right:108px}
.social span{width:20px;height:20px;background:#3e6d9c;color:#fff;font-size:0;display:block}
.social-names{top:34px;right:108px;font-size:6px;color:#8a96a3;letter-spacing:.2px}
.head-rule{left:518px;top:44px;width:174px;height:1px;background:var(--line)}
.head-btn{top:54px;height:22px;background:var(--btn-dark);color:#fff;font-family:'Roboto',sans-serif;font-size:9.5px;display:flex;align-items:center;justify-content:center;gap:4px;border:1px solid #39424b}
/* nav */
.nav{left:0;top:88px;width:800px;height:34px;background:var(--brand)}
.nav ul{list-style:none;position:absolute;left:107px;top:0;display:flex;height:34px;align-items:center;gap:19px}
.nav li{font-family:'Roboto',sans-serif;font-size:7.6px;color:#fff;text-transform:uppercase}
.nav li.active{color:#0b3d66}
.nav-caret{left:114px;top:117px;width:0;height:0;border-left:5px solid transparent;border-right:5px solid transparent;border-bottom:5px solid #fff}
.search{left:591px;top:96px;width:101px;height:19px;background:#0780b5;border:1px solid #0a6f9e}
.search-btn{left:673px;top:96px;width:19px;height:19px;background:#0a6aa0}
/* hero */
.hero{left:0;top:122px;width:800px;height:258px;background:linear-gradient(#fff,#f1f2f3);border-bottom:1px solid var(--line)}
.video{left:108px;top:138px;width:342px;height:228px;background:linear-gradient(135deg,#5b5e62,#2f3237 60%,#1d1f22)}
.video-text{left:108px;top:192px;width:342px;text-align:center;font-family:'Roboto',sans-serif;font-weight:300;color:#f2f2f2;font-size:22px;line-height:34px}
.video-bar{left:108px;top:338px;width:342px;height:28px;background:#1a1b1d}
.progress{left:158px;top:350px;width:212px;height:4px;background:#3a3c40;border-radius:2px}
.progress i{display:block;width:108px;height:4px;background:var(--brand);border-radius:2px}
.video-time{left:385px;top:347px;font-size:6.5px;color:#ddd}
.hero-title{left:474px;top:170px;width:220px;font-family:'Roboto',sans-serif;font-size:12.5px;line-height:15px;color:var(--brand)}
.hero-title b{font-weight:400;color:#333}
.hero-list{left:488px;top:216px;width:200px;list-style:none}
.hero-list li{font-size:8.8px;color:#555;line-height:11px;margin-bottom:11px;position:relative}
.hero-list li:before{content:"›";position:absolute;left:-14px;top:-1px;font-size:11px;color:#666}
/* pricing */
.plan{color:#fff;text-align:center;box-shadow:0 2px 4px rgba(0,0,0,.15)}
.plan.side{background:var(--brand-deep)}
.plan.main{background:var(--brand);z-index:2}
.plan h3{font-family:'Roboto',sans-serif;font-weight:300;font-size:21px;line-height:22px}
.plan .price{font-family:'Roboto',sans-serif;font-size:17px;font-weight:500;margin-top:4px}
.plan .price small{font-size:12px;font-weight:300}
.plan hr{border:0;height:1px;background:rgba(255,255,255,.25);margin:14px 16px 16px}
.plan ul{list-style:none;text-align:left;padding:0 18px 0 32px}
.plan li{font-size:8px;line-height:11.5px;margin-bottom:8.5px;position:relative}
.plan li:before{content:"›";position:absolute;left:-16px;top:-1px;width:10px;height:10px;border-radius:50%;background:#fff;color:var(--brand-deep);font-size:10px;line-height:9px;text-align:center;font-weight:600}
/* band */
.band{left:0;top:723px;width:800px;height:271px;background:var(--band)}
.band-text{left:0;top:737px;width:800px;text-align:center;font-size:11px;color:#444}
.mail-btn{left:303px;top:762px;width:194px;height:28px;background:var(--brand);color:#fff;font-size:9.5px;display:flex;align-items:center;justify-content:center}
/* lower */
.sec-title{font-family:'Roboto',sans-serif;font-size:12px;color:var(--brand);font-weight:500}
.pager{font-size:13px;color:var(--brand);letter-spacing:5px}
.avatar{left:107px;top:862px;width:46px;height:46px;border-radius:50%;background:linear-gradient(#cfd6dc,#8c99a4);border:2px solid #fff;box-shadow:0 0 0 1px #ccc}
.quote{left:163px;top:861px;width:146px;font-size:7.7px;line-height:10.5px;color:#444}
.quote-mark{left:298px;top:898px;font-family:Georgia,serif;font-size:24px;color:#999}
.author{left:107px;top:916px;font-style:italic;font-size:8.6px;color:var(--brand)}
.divider{left:325px;top:830px;width:1px;height:112px;background:var(--line)}
.tip-date{width:28px;height:28px;background:var(--brand);color:#fff;font-size:7.5px;line-height:9px;text-align:center;padding-top:5px}
.tip-text{width:156px;font-size:7.7px;line-height:9.6px;color:#444}
/* calendar */
.cal{left:557px;top:828px;width:125px;height:124px;background:#fff;box-shadow:0 2px 3px rgba(0,0,0,.2)}
.cal-head{height:18px;background:var(--brand-deep);color:#fff;font-family:'Roboto',sans-serif;font-size:10px;display:flex;align-items:center;justify-content:space-between;padding:0 5px}
.cal table{border-collapse:collapse;width:125px}
.cal th{font-size:5px;color:#999;font-weight:400;height:10px}
.cal td{font-size:7.5px;text-align:center;height:17.6px;width:17.8px;border:1px solid #e4e4e4;color:#333}
.cal td.today{background:#e8e8e8;color:#888}
/* footer */
.footer{left:0;top:994px;width:800px;height:206px;background:var(--navy)}
.foot-bottom{left:0;top:1165px;width:800px;height:35px;background:var(--navy-dark)}
.up{left:380px;top:974px;width:40px;height:40px;border-radius:50%;background:#fff}
.foot-title{font-family:'Roboto',sans-serif;font-size:13px;color:#fff}
.foot-title span{color:var(--brand)}
.sitemap{left:107px;top:1056px;width:236px;display:grid;grid-template-columns:112px 112px;column-gap:12px}
.sitemap div{font-size:7.5px;color:#cfd8e6;height:25.6px;border-bottom:1px solid #1e4a80;padding-top:6px}
.sitemap div.on{color:#f5b400}
.field{background:#051d40;border:1px solid #1f4a7d;color:#a9b7c9;font-size:7.5px;padding:6px}
.send{left:546px;top:1112px;width:70px;height:22px;background:var(--brand);color:#fff;font-size:9.5px;display:flex;align-items:center;justify-content:center;border:1px solid #3cb4e6}
.pay{left:104px;top:1172px;font-family:'Open Sans',sans-serif;font-weight:600;font-size:16px;color:var(--brand)}
.copy{right:108px;top:1178px;font-size:7.5px;color:#a9b7c9}
.copy span{color:var(--brand)}
</style>
</head>
<body>
<!-- header -->
<div class="abs logo"><span class="logo-mark"></span><span class="logo-name">QUOLT</span></div>
<div class="abs logo-sub">Online Tuition</div>
<div class="abs social" aria-label="friendwall, chirplo, talqo"><span></span><span></span><span></span></div>
<div class="abs head-rule"></div>
<div class="abs head-btn" style="left:526px;width:80px">
  <svg width="7" height="9" viewBox="0 0 7 9"><path d="M3.5 0A3 3 0 0 0 .5 3c0 2.2 3 6 3 6s3-3.8 3-6a3 3 0 0 0-3-3zm0 4.2a1.2 1.2 0 1 1 0-2.4 1.2 1.2 0 0 1 0 2.4z" fill="#fff"/></svg>Enroll Here</div>
<div class="abs head-btn" style="left:612px;width:80px">
  <svg width="7" height="9" viewBox="0 0 7 9"><rect x="0" y="4" width="7" height="5" fill="#fff"/><path d="M1.5 4V2.5a2 2 0 0 1 4 0V4" stroke="#fff" fill="none"/></svg>Students Login</div>

<!-- navigation -->
<nav class="abs nav"><ul>
  <li class="active">Home</li><li>Tutorial Packages</li><li>Weekly Tips &amp; Comments</li><li>Reading</li><li>Speaking</li><li>Listening</li><li>Writing</li>
</ul></nav>
<div class="abs nav-caret"></div>
<div class="abs search"></div>
<div class="abs search-btn"><svg width="19" height="19" viewBox="0 0 19 19"><circle cx="8.5" cy="8.5" r="3" stroke="#fff" stroke-width="1.4" fill="none"/><line x1="10.7" y1="10.7" x2="13" y2="13" stroke="#fff" stroke-width="1.6"/></svg></div>

<!-- hero -->
<div class="abs hero"></div>
<div class="abs video" role="img" aria-label="Video still: student writing notes at a library desk"></div>
<div class="abs video-text">We put you first!<br>We listen to you and help<br>you find what you need.</div>
<svg class="abs" style="left:272px;top:230px" width="12" height="16" viewBox="0 0 12 16"><path d="M0 0l12 8-12 8z" fill="#fff"/></svg>
<div class="abs video-bar"></div>
<svg class="abs" style="left:116px;top:347px" width="8" height="9" viewBox="0 0 8 9"><path d="M0 0l8 4.5L0 9z" fill="#fff"/></svg>
<svg class="abs" style="left:140px;top:348px" width="10" height="8" viewBox="0 0 10 8"><path d="M0 2.5h2L5 0v8L2 5.5H0z" fill="#999"/><path d="M7 2q1.5 2 0 4" stroke="#999" fill="none"/></svg>
<div class="abs progress"><i></i></div>
<div class="abs video-time">11:57</div>
<svg class="abs" style="left:427px;top:346px" width="11" height="11" viewBox="0 0 11 11"><path d="M1 10L10 1M6 1h4v4M1 6v4h4" stroke="#ddd" stroke-width="1.3" fill="none"/></svg>
<div class="abs hero-title">If you want help in passing an <b>QUOLT</b> test, we can help you with:</div>
<ul class="abs hero-list">
  <li>Lessons in reading, writing, listening and speaking</li>
  <li>Professional teacher feedback and tips.</li>
  <li>Talqo and practice with native speakers.</li>
  <li>Quick Turnaround.</li>
  <li>Friendly and Approachable teachers.</li>
</ul>

<!-- grey band with arrows -->
<div class="abs band"></div>
<svg class="abs" style="left:200px;top:680px" width="400" height="70" viewBox="0 0 400 70">
  <path d="M16 0C20 30 45 55 78 66" stroke="var(--brand-deep)" stroke-width="1.5" fill="none"/>
  <path d="M78 66L48 60 62 58 54 46z" fill="var(--brand-deep)"/>
  <path d="M384 0C380 30 355 55 322 66" stroke="var(--brand-deep)" stroke-width="1.5" fill="none"/>
  <path d="M322 66L352 60 338 58 346 46z" fill="var(--brand-deep)"/>
</svg>

<!-- pricing -->
<section class="abs plan side" style="left:120px;top:423px;width:185px;height:257px;padding-top:14px">
  <h3>Silver</h3><div class="price">$20/<small>Month</small></div><hr>
  <ul><li>45 days access</li><li>25 hours study time</li><li>Over 190 Study Pages</li><li>100 Interactive Activities</li><li>Practice tests in all 4 modules</li><li>and more ...</li></ul>
</section>
<section class="abs plan main" style="left:303px;top:409px;width:194px;height:285px;padding-top:14px">
  <h3>Diamond</h3><div class="price">$50/<small>Month</small></div><hr>
  <ul><li>90 days access</li><li>100 hours study time</li><li>Over 1000 Study Pages</li><li>Over 260 Interactive Activities</li><li>Detailed advice and model answers for all activities</li><li>Voice recording tools</li><li>Individual feedback on two writing tasks</li><li>and more...</li></ul>
</section>
<section class="abs plan side" style="left:497px;top:423px;width:183px;height:257px;padding-top:14px">
  <h3>Gold</h3><div class="price">$35/<small>Month</small></div><hr>
  <ul><li>90 days access</li><li>Over 1000 Study Pages</li><li>100 hours study time</li><li>Voice recording tools</li><li>Detailed advice and model answers for all activities</li><li>Over 260 Interactive Activities</li><li>and more...</li></ul>
</section>

<div class="abs band-text">Trace-out our online Tutorial Packages !</div>
<div class="abs mail-btn">packages@lingvarotutors.example</div>

<!-- testimonials -->
<div class="abs sec-title" style="left:107px;top:824px">Experience from our Students</div>
<div class="abs pager" style="left:293px;top:822px">‹›</div>
<div class="abs avatar" role="img" aria-label="Student portrait"></div>
<p class="abs quote">Lorem Ipsum is simply dummy text of the printing and typesetting industry. Lorem Ipsum has been the industry's standard dummy text ever since the 1500s, when an unknown printer</p>
<div class="abs quote-mark">”</div>
<div class="abs author">Dario Menck</div>
<div class="abs divider"></div>

<!-- tips -->
<div class="abs sec-title" style="left:337px;top:824px">Weekly Tips &amp; Tricks</div>
<div class="abs pager" style="left:511px;top:822px">‹›</div>
<div class="abs tip-date" style="left:337px;top:860px">05<br>Jan</div>
<p class="abs tip-text" style="left:377px;top:860px">Contrary to popular belief, Lorem Ipsum is not simply random text. It has roots in a piece of classical Latin &nbsp;[ .. ]</p>
<div class="abs tip-date" style="left:337px;top:900px">12<br>Jan</div>
<p class="abs tip-text" style="left:377px;top:900px">Contrary to popular belief, Lorem Ipsum is not simply random text. It has roots in a piece of classical Latin &nbsp;[ .. ]</p>

<!-- calendar -->
<div class="abs cal">
  <div class="cal-head"><span>‹</span><span>January 2014</span><span>›</span></div>
  <table>
    <tr><th>SUN</th><th>MON</th><th>TUE</th><th>WED</th><th>THU</th><th>FRI</th><th>SAT</th></tr>
    <tr><td></td><td>1</td><td>2</td><td>3</td><td>4</td><td>5</td><td>6</td></tr>
    <tr><td>7</td><td>8</td><td>9</td><td>10</td><td>11</td><td class="today">12</td><td>13</td></tr>
    <tr><td>14</td><td>15</td><td>16</td><td>17</td><td>18</td><td>19</td><td>20</td></tr>
    <tr><td>21</td><td>22</td><td>23</td><td>24</td><td>25</td><td>26</td><td>27</td></tr>
    <tr><td>28</td><td>29</td><td>30</td><td>31</td><td></td><td></td><td></td></tr>
  </table>
</div>

<!-- footer -->
<footer class="abs footer"></footer>
<div class="abs foot-bottom"></div>
<div class="abs up"><svg width="40" height="40" viewBox="0 0 40 40"><path d="M12 23l8-7 8 7" stroke="#5aa8d8" stroke-width="2" fill="none"/></svg></div>
<div class="abs foot-title" style="left:107px;top:1032px">Our <span>Sitemap</span></div>
<div class="abs sitemap">
  <div class="on">›&nbsp; Home</div><div>›&nbsp; Tutorial Packages</div>
  <div>›&nbsp; Weekly Tips &amp; Comments</div><div>›&nbsp; Reading</div>
  <div>›&nbsp; Speaking</div><div>›&nbsp; Listening</div>
  <div>›&nbsp; Writing</div><div>›&nbsp; Contact</div>
</div>
<div class="abs foot-title" style="left:383px;top:1032px">Quick <span>Contact</span></div>
<div class="abs field" style="left:384px;top:1057px;width:146px;height:20px">Name</div>
<div class="abs field" style="left:384px;top:1086px;width:146px;height:20px">Email</div>
<div class="abs field" style="left:384px;top:1115px;width:146px;height:20px">Contact No.</div>
<div class="abs field" style="left:546px;top:1057px;width:146px;height:47px">Comment / Enquiry</div>
<div class="abs send">SEND</div>
<div class="abs pay">payvora</div>
<div class="abs copy"><span>Marlowe Studio</span> ©2014. All Rights Reserved.</div>
</body>
</html>
```